New Website for Belcourt Manor at www.belcourt.com.au

A new logo has been designed (through pixel forge) and we now want to align the look and feel of our website at www.belcourt.com.au to the new logo. The content and page names (e.g. Grounds) will remain largely unchanged for the new site, so please submit a new look "Home" page, using our new logo, current text and any photos you choose from the existing gallery at our website. I have also attached the current "Home" page photos.

Industry/Entity Type

Accommodation

Number of Pages Required

1 page

Requirements
Must have
• Logo to be presented on white background.

```html
<!DOCTYPE html>
<html lang="en">
<head>
<meta charset="utf-8">
<title>Belcourt Manor – Home</title>
<link rel="stylesheet" href="https://fonts.googleapis.com/css2?family=Open+Sans:wght@300;400;600&display=swap">
<style>
  :root {
    --white: #ffffff;
    --ink: #222222;
    --text: #333333;
    --muted: #555555;
    --soft-bg: #f2f2f2;
    --rule: #d6d6d6;
    --brand-blue: #1a6fb5;
    --active: #2a8fd4;
  }
  * { box-sizing: border-box; margin: 0; padding: 0; }
  html, body { width: 854px; height: 1200px; overflow: hidden; background: var(--white); }
  body { font-family: "Open Sans", Arial, sans-serif; color: var(--text); position: relative; }

  .site-header { position: absolute; top: 0; left: 0; width: 854px; height: 56px; background: var(--white); border-bottom: 1px solid #e4e4e4; }
  .brand { position: absolute; left: 128px; top: 14px; display: flex; align-items: center; gap: 7px; font-size: 20px; font-weight: 400; color: var(--brand-blue); text-decoration: none; }
  .brand-dot { width: 14px; height: 14px; border-radius: 50%; background: #f2c230; }
  .main-nav { position: absolute; top: 0; left: 0; height: 56px; width: 854px; }
  .main-nav a { position: absolute; top: 23px; font-size: 7.5px; color: var(--ink); text-decoration: none; }
  .main-nav a.active::after { content: ""; position: absolute; left: -4px; right: -4px; top: 32px; height: 2px; background: var(--active); }
  .caret { display: inline-block; margin-left: 3px; border: 3px solid transparent; border-top-color: #aaa; vertical-align: -2px; }
  .menu-icon { position: absolute; left: 729px; top: 25px; }

  .hero { position: absolute; top: 56px; left: 0; width: 854px; height: 338px;
    background: linear-gradient(160deg, #5f8a3c 0%, #c9a77a 35%, #b8563a 55%, #c6b49a 70%, #6f9146 100%); }
  .hero-title { position: absolute; left: 0; width: 854px; top: 140px; text-align: center; color: var(--white); font-size: 40px; font-weight: 300; letter-spacing: 1px; }
  .hero-sub { position: absolute; left: 0; width: 854px; top: 196px; text-align: center; color: var(--white); font-size: 12px; letter-spacing: 1px; }
  .hero-cta { position: absolute; left: 366px; top: 253px; width: 122px; height: 32px; border: 1px solid rgba(255,255,255,.8); background: rgba(235,235,235,.75); color: var(--ink); font-size: 9.5px; text-align: center; line-height: 30px; text-decoration: none; }
  .slider-dots { position: absolute; left: 701px; top: 279px; display: flex; gap: 4px; }
  .slider-dots span { width: 6px; height: 6px; border-radius: 50%; border: 1px solid var(--white); }
  .slider-dots span.on { background: var(--white); }

  .intro { position: absolute; top: 394px; left: 0; width: 854px; height: 192px; background: var(--white); }
  .intro-heading { position: absolute; right: 473px; top: 44px; text-align: right; font-size: 26px; font-weight: 400; line-height: 32px; color: var(--ink); letter-spacing: .3px; }
  .intro-copy { position: absolute; left: 418px; top: 17px; width: 322px; font-size: 9.8px; line-height: 12.8px; color: var(--ink); text-align: justify; }
  .intro-copy p { margin-bottom: 12.8px; }
  .intro-copy a { color: var(--ink); }

  .gallery { position: absolute; top: 586px; left: 0; width: 854px; height: 422px; background: var(--soft-bg); }
  .photo { position: absolute; }
  .photo-lounge { left: 115px; top: 31px; width: 410px; height: 158px; background: linear-gradient(135deg, #c8c2b4, #b06a3a 45%, #8a4d2a 80%, #d9cbb5); }
  .photo-hall { left: 542px; top: 31px; width: 196px; height: 158px; background: linear-gradient(120deg, #b87a3a 0%, #e9dcc4 35%, #8fb1c9 75%, #6d8fa8); }
  .photo-bar { left: 115px; top: 206px; width: 196px; height: 158px; background: linear-gradient(120deg, #1f3a6a 0%, #6b5a3a 40%, #d9a35c 70%, #3a2e22); }
  .photo-bath { left: 329px; top: 206px; width: 409px; height: 158px; background: linear-gradient(180deg, #e4e6e6 0%, #c9cccc 65%, #6f7878 100%); }

  .cta-band { position: absolute; top: 1008px; left: 0; width: 854px; height: 58px; background: var(--white); }
  .cta-button { position: absolute; left: 328px; top: 6px; width: 168px; height: 47px; border: 1px solid #777; color: var(--ink); font-size: 15px; text-align: center; line-height: 45px; text-decoration: none; }

  .spacer-band { position: absolute; top: 1066px; left: 0; width: 854px; height: 56px; background: var(--soft-bg); }

  .site-footer { position: absolute; top: 1122px; left: 0; width: 854px; height: 78px; background: var(--white); }
  .footer-nav { position: absolute; top: 10px; left: 0; width: 854px; text-align: center; font-size: 8.8px; color: var(--ink); }
  .footer-nav a { color: var(--ink); text-decoration: none; }
  .footer-nav .sep { margin: 0 4px; }
  .footer-rule { position: absolute; top: 40px; left: 328px; width: 198px; height: 1px; background: var(--rule); }
  .copyright { position: absolute; top: 54px; left: 0; width: 854px; text-align: center; font-size: 8px; color: var(--muted); }
</style>
</head>
<body>

<header class="site-header">
  <a class="brand" href="#"><span class="brand-dot"></span>Belcourt Manor</a>
  <nav class="main-nav">
    <a class="active" href="#" style="left:434px">Home</a>
    <a href="#" style="left:486px">Gallery</a>
    <a href="#" style="left:542px">Mansion<span class="caret"></span></a>
    <a href="#" style="left:610px">Location</a>
    <a href="#" style="left:679px">Contact</a>
    <svg class="menu-icon" width="9" height="7" viewBox="0 0 9 7" aria-label="Menu"><rect y="0" width="9" height="1.2" fill="#222"/><rect y="2.9" width="9" height="1.2" fill="#222"/><rect y="5.8" width="9" height="1.2" fill="#222"/></svg>
  </nav>
</header>

<section class="hero" role="img" aria-label="Aerial photo of the manor with terracotta roofs, gravel driveway, palms and lawns">
  <div class="hero-title">Belcourt</div>
  <div class="hero-sub">MANOR</div>
  <a class="hero-cta" href="#">BOOK NOW</a>
  <div class="slider-dots"><span></span><span></span><span></span><span class="on"></span></div>
</section>

<section class="intro">
  <h1 class="intro-heading">PALATIAL ESTATE<br>AND<br>LUXURY RESORT</h1>
  <div class="intro-copy">
    <p>On over 2 manicured garden acres, Belcourt Manor is a unique Silver Coast estate, centrally located in the prestigious rural suburb of Larkhill. <a href="#">More about our Location</a></p>
    <p>The estate features a grand mansion, private pub (The Fox and Hare), sparkling resort pool, tennis court and playground.</p>
    <p>Magnificent properties rarely feel so warm and welcoming – so browse away and visit our photo gallery<br>– and we look forward to having you stay as our guests.</p>
    <p>For prices, availability and guest reviews, visit <a href="#">Holidaze</a>.</p>
  </div>
</section>

<section class="gallery">
  <div class="photo photo-lounge" role="img" aria-label="Lounge room with black leather sofas on terracotta tiles"></div>
  <div class="photo photo-hall" role="img" aria-label="Upstairs hallway with framed artwork and arched balustrade"></div>
  <div class="photo photo-bar" role="img" aria-label="Evening view of the deck opening into the private pub"></div>
  <div class="photo photo-bath" role="img" aria-label="Marble bathroom with columns and spa bath"></div>
</section>

<section class="cta-band">
  <a class="cta-button" href="#">BOOK NOW</a>
</section>

<div class="spacer-band"></div>

<footer class="site-footer">
  <nav class="footer-nav">
    <a href="#">Home</a><span class="sep">|</span><a href="#">Mansion</a><span class="sep">|</span><a href="#">Bedrooms</a><span class="sep">|</span><a href="#">Options</a><span class="sep">|</span><a href="#">Fox and Hare</a><span class="sep">|</span><a href="#">Grounds</a><span class="sep">|</span><a href="#">Location</a><span class="sep">|</span><a href="#">Gallery</a><span class="sep">|</span><a href="#">Contact</a><span class="sep">|</span><a href="#">Availability</a><span class="sep">|</span><a href="#">DIY Weddings</a>
  </nav>
  <div class="footer-rule"></div>
  <p class="copyright">Copyright © 2016 Belcourt Manor. All Rights Reserved.</p>
</footer>

</body>
</html>
```